KLV Home Loans Website

Need a web site designed for a Professional Mortgage company along the lines of the draft site www.klvhomeloans.com.au

The main purpose of the site is to provide a professional image of the company and capture email address's and send out simple messages. ie "INTEREST RATE SPECIAL 4.5% FOR THE MONTH OF JUNE" or whatever...basically short punchy messages to hook people.

The content is important but a lot of that can be provided by links to our lender panel, several of which have been set up.

Most people will want to know current interest rates, and how much they can borrow along with what it will cost. There are various calculators embedded in the lenders sites such as "Repayment Calculators" Borrow Capacity Calculators" Stamp Duty Calculators"

These would be nice to have on site, but if to costly or difficult to start the links can suffice.

The site will need to be updated/amended regularily.

Example "Interest Rate Special" or "Current Special Offer" sections would be required and would need to be easyily editable and in fact would need to be able to switch them off if there is no special running.

Target Market(s)

Target market is a broad spectrum of people from young couple buying first home to older couples investing.

Industry/Entity Type

It Company

Requirements
Must have
• email capture, preferably need to enter email to enter site.

```html
<!DOCTYPE html>
<html lang="en">
<head>
<meta charset="utf-8">
<title>KLV Home Loans</title>
<link href="https://fonts.googleapis.com/css2?family=Open+Sans:wght@400;600;700&family=Roboto+Condensed:wght@400&family=Arimo:wght@400;700&display=swap" rel="stylesheet">
<style>
:root{
  --nav-top:#3a3a3a;
  --nav-bottom:#151515;
  --ink:#2b2b2b;
  --muted:#555;
  --accent:#1b3f9c;
  --link-blue:#1e5fb4;
  --band-light:#2d6bcc;
  --band-dark:#1a46a6;
  --button-top:#5db6f0;
  --button-bottom:#2f8fd8;
  --amber:#f5a81c;
  --note:#d9f28c;
  --footer-light:#1f46b0;
  --footer-dark:#0b2585;
  --footer-text:#c9d3ef;
  --footer-head:#8fa3da;
  --panel:#2c2c2c;
  --bar:#1b1b1b;
  --white:#fff;
}
*{box-sizing:border-box;margin:0;padding:0}
html,body{width:886px;height:1200px;overflow:hidden}
body{position:relative;background:var(--white);font-family:"Arimo",Arial,sans-serif;color:var(--ink)}
a{color:inherit;text-decoration:none}
.abs{position:absolute}

/* header */
.site-header{position:absolute;left:0;top:0;width:886px;height:55px;background:linear-gradient(var(--nav-top),var(--nav-bottom))}
.brand{position:absolute;left:120px;top:15px;font-family:"Open Sans",sans-serif;font-weight:700;font-size:20px;color:var(--white);letter-spacing:-.2px}
.main-nav{position:absolute;top:22px;left:0;font-family:"Open Sans",sans-serif;font-weight:600;font-size:11.5px;color:var(--white)}
.main-nav a{position:absolute;white-space:nowrap}
.main-nav .current{text-shadow:0 0 6px rgba(255,255,255,.5)}

/* hero */
.hero{position:absolute;left:0;top:55px;width:886px;height:313px;background:var(--white);overflow:hidden}
.hero-visual{position:absolute;left:321px;top:0;width:565px;height:313px;background:radial-gradient(ellipse at 45% 45%,#e7b28e 0%,#c9ccd6 28%,#eef0f4 55%,#fff 80%)}
.hero-title{position:absolute;left:120px;top:76px;font-family:"Open Sans",sans-serif;font-weight:700;font-size:20.5px;line-height:25px;color:var(--ink)}
.hero-title .rate{color:var(--accent)}
.hero-text{position:absolute;left:123px;top:142px;width:255px;font-size:8.4px;line-height:13px;color:var(--muted);font-weight:700}
.btn-learn{position:absolute;left:119px;top:193px;width:111px;height:36px;border-radius:3px;background:linear-gradient(var(--button-top),var(--button-bottom));color:var(--white);font-family:"Open Sans",sans-serif;font-weight:600;font-size:12px;text-align:center;line-height:36px;box-shadow:0 1px 2px rgba(0,0,0,.25)}

/* signup band */
.signup{position:absolute;left:0;top:368px;width:886px;height:160px;background:radial-gradient(ellipse at 50% 30%,var(--band-light),var(--band-dark) 75%);text-align:center}
.signup h2{position:absolute;left:0;width:886px;top:23px;font-family:"Open Sans",sans-serif;font-weight:700;font-size:20.5px;color:var(--white)}
.signup-field{position:absolute;left:166px;top:63px;width:340px;height:37px;background:#e4e4e4;border:0;font-family:"Open Sans",sans-serif;font-size:14px;color:#666;padding-left:15px;text-align:left;line-height:37px}
.signup-btn{position:absolute;left:506px;top:63px;width:150px;height:37px;background:var(--amber);color:#8a5a05;font-family:"Open Sans",sans-serif;font-weight:600;font-size:14px;line-height:37px;display:flex;align-items:center;justify-content:center;gap:6px}
.signup-note{position:absolute;left:0;width:886px;top:111px;font-size:9.5px;color:var(--note)}
.signup-note u{color:var(--note)}

/* features */
.feature{position:absolute;top:572px;width:205px}
.feature h3{font-family:"Roboto Condensed",sans-serif;font-weight:400;font-size:13px;letter-spacing:.6px;color:#444;text-transform:uppercase}
.feature-media{margin-top:9px;width:205px;height:96px}
.media-papers{background:linear-gradient(135deg,#d9d9d9,#f2f2f2 45%,#8a8a8a 80%,#3a3f4e)}
.media-calc{background:linear-gradient(135deg,#eaeaea,#c9cbd0 45%,#5a5c63 75%,#e9a06a)}
.media-cabin{background:linear-gradient(#7fb6e4 0%,#c6ddef 30%,#c9553d 45%,#c98550 70%,#6f9a3e 100%)}
.feature p{margin-top:13px;font-size:7.5px;line-height:11.6px;color:#333}
.feature .more{display:block;margin-top:14px;font-size:7.4px;font-weight:700;color:var(--link-blue);letter-spacing:.3px}

/* footer */
.site-footer{position:absolute;left:0;top:820px;width:886px;height:329px;background:radial-gradient(ellipse at 25% 10%,var(--footer-light),var(--footer-dark) 70%);color:var(--footer-text)}
.footer-logo{position:absolute;left:120px;top:67px;font-family:"Arimo",sans-serif;font-size:25px;color:#14276e;letter-spacing:1px}
.footer-head{position:absolute;font-family:"Arimo",sans-serif;font-size:11.5px;letter-spacing:.6px;color:var(--footer-head);text-transform:uppercase}
.footer-copy{position:absolute;font-size:7.2px;line-height:12px;color:var(--footer-text)}
.contact-line{position:absolute;left:437px;font-size:7.2px;font-weight:700;color:var(--white);display:flex;align-items:center;gap:10px}
.contact-line svg{width:10px;height:10px;fill:#9aa6c8}
.newsletter{position:absolute;left:602px;top:31px;width:166px;height:110px;background:var(--panel)}
.newsletter h4{position:absolute;left:32px;top:8px;font-size:7.4px;font-weight:700;color:var(--white)}
.newsletter .mail{position:absolute;left:11px;top:8px}
.newsletter p{position:absolute;left:11px;top:25px;font-size:7px;color:#ccc}
.newsletter .nl-field{position:absolute;left:11px;top:43px;width:144px;height:21px;background:#e6e6e6;font-size:6.5px;color:#555;line-height:21px;padding-left:8px}
.newsletter .nl-btn{position:absolute;left:11px;top:74px;width:144px;height:22px;background:#1534a0;color:var(--white);font-weight:700;font-size:9.5px;letter-spacing:.5px;text-align:center;line-height:22px}
.footer-rule{position:absolute;left:120px;top:166px;width:648px;height:1px;background:rgba(255,255,255,.15)}
.link-list{position:absolute;top:221px;list-style:none;font-size:7px;font-weight:700;color:var(--white)}
.link-list li{height:13.3px;line-height:13.3px}
.link-list li::before{content:"›";color:#9aa6c8;margin-right:7px}
.social-list{position:absolute;left:602px;top:221px;list-style:none;font-size:7px;font-weight:700;color:var(--white)}
.social-list li{height:21.3px;display:flex;align-items:center;gap:9px}
.social-list .dot{width:13px;height:13px;border-radius:50%;background:#6b7595}

/* bottom bar */
.legal-bar{position:absolute;left:0;top:1149px;width:886px;height:51px;background:var(--bar);color:#ddd;font-size:7.4px}
.legal-bar .copyright{position:absolute;left:120px;top:19px}
.legal-links{position:absolute;left:601px;top:19px;display:flex;gap:9px}
.legal-links .sep{color:#999}
</style>
</head>
<body>

<header class="site-header">
  <a class="brand" href="#">KLV Home Loans</a>
  <nav class="main-nav">
    <a class="current" href="#" style="left:484px">Home</a>
    <a href="#" style="left:534px">Services</a>
    <a href="#" style="left:598px">Partners</a>
    <a href="#" style="left:657px">About</a>
    <a href="#" style="left:709px">Contact</a>
  </nav>
</header>

<section class="hero">
  <div class="hero-visual" role="img" aria-label="Photo of a model house with a hand holding a pen over loan papers"></div>
  <h1 class="hero-title">Special Interest Rate of <span class="rate">4.5%</span><br>for the month of June.</h1>
  <p class="hero-text">KLV Home Loans offers a complete range of finance solutions tailored to meet individual client needs.</p>
  <a class="btn-learn" href="#">Learn More</a>
</section>

<section class="signup">
  <h2>Enter your email and receive exclusive special rates!</h2>
  <div class="signup-field">Your Email Address..</div>
  <div class="signup-btn">
    <svg width="11" height="11" viewBox="0 0 12 12"><path d="M1 11l1-3 6-6 2 2-6 6z" fill="#8a5a05"/></svg>
    Sign up for FREE
  </div>
  <p class="signup-note">Your email will be held in strictest of confidentiality. <u>Privacy Policy</u></p>
</section>

<article class="feature" style="left:120px">
  <h3>Our Services</h3>
  <div class="feature-media media-papers" role="img" aria-label="Photo of loan application papers and folders"></div>
  <p>Lorem ipsum dolor sit amet, consectetur adipisicing elit, sed do eiusmod tempor incididunt ut labore et dolore magna aliqua. Ut enim ad minim veniam, quis nostrud exercitation.</p>
  <a class="more" href="#">READ MORE ›</a>
</article>
<article class="feature" style="left:341px">
  <h3>Repayment Calculators</h3>
  <div class="feature-media media-calc" role="img" aria-label="Photo of a calculator with glasses and a pen"></div>
  <p>Lorem ipsum dolor sit amet, consectetur adipisicing elit, sed do eiusmod tempor incididunt ut labore et dolore magna aliqua. Ut enim ad minim veniam, quis nostrud exercitation.</p>
  <a class="more" href="#">READ MORE ›</a>
</article>
<article class="feature" style="left:563px">
  <h3>Current Special Offer</h3>
  <div class="feature-media media-cabin" role="img" aria-label="Photo of a timber house with a red roof"></div>
  <p>Lorem ipsum dolor sit amet, consectetur adipisicing elit, sed do eiusmod tempor incididunt ut labore et dolore magna aliqua. Ut enim ad minim veniam, quis nostrud exercitation.</p>
  <a class="more" href="#">READ MORE ›</a>
</article>

<footer class="site-footer">
  <div class="footer-logo">LOGO</div>

  <h4 class="footer-head" style="left:269px;top:31px">What We Do</h4>
  <p class="footer-copy" style="left:269px;top:52px;width:120px">Duis mollis, est non commodo luctus, nisi erat porttitor ligula, eget lacinia odio sem nec elit. Vestibulum id ligula porta felis euismod semper. Integer posuere erat a ante.</p>
  <p class="footer-copy" style="left:269px;top:121px;width:125px">Vestibulum id ligula porta felis euismod semper. Integer posuere erat a ante.</p>

  <h4 class="footer-head" style="left:434px;top:31px">Contact</h4>
  <p class="footer-copy" style="left:437px;top:54px;width:120px">There are many variations of passages of Lorem Ipsum available, but the majority have suffered alteration.</p>
  <div class="contact-line" style="top:98px">
    <svg viewBox="0 0 10 10"><path d="M5 0a3.5 3.5 0 0 0-3.5 3.5C1.5 6 5 10 5 10s3.5-4 3.5-6.5A3.5 3.5 0 0 0 5 0zm0 5a1.4 1.4 0 1 1 0-2.8A1.4 1.4 0 0 1 5 5z"/></svg>
    Harbour Street
  </div>
  <div class="contact-line" style="top:115px">
    <svg viewBox="0 0 10 10"><path d="M0 2h10v6H0z"/><path d="M0 2l5 3.5L10 2" stroke="#1a3a9a" fill="none"/></svg>
    hello@klvhomeloans.com.au
  </div>
  <div class="contact-line" style="top:132px">
    <svg viewBox="0 0 10 10"><path d="M2 0l2 2.5-1 1.2c.8 1.5 1.8 2.5 3.3 3.3l1.2-1L10 8l-1.5 2C4 9.5.5 6 0 1.5z"/></svg>
    03-5550-1427
  </div>

  <div class="newsletter">
    <svg class="mail" width="13" height="9" viewBox="0 0 13 9"><rect width="13" height="9" fill="#888"/><path d="M0 0l6.5 5L13 0" stroke="#2c2c2c" fill="none"/></svg>
    <h4>SUBSCRIBE TO OUR NEWSLETTER</h4>
    <p>Sign up and get the latest news and updates.</p>
    <div class="nl-field">Enter your email address</div>
    <div class="nl-btn">SUBSCRIBE TODAY</div>
  </div>

  <div class="footer-rule"></div>

  <h4 class="footer-head" style="left:120px;top:198px">Site Links</h4>
  <ul class="link-list" style="left:120px">
    <li>Home</li><li>About</li><li>Services</li><li>Partners</li><li>Contact</li>
  </ul>

  <h4 class="footer-head" style="left:285px;top:198px">Services</h4>
  <ul class="link-list" style="left:285px">
    <li>New Home</li><li>First Home Owner Mortgage</li><li>Refinance</li><li>Investmentt</li>
  </ul>
  <ul class="link-list" style="left:435px">
    <li>Bridging</li><li>Car Loan</li><li>Plant &amp; Equipment</li><li>Insurance</li>
  </ul>

  <h4 class="footer-head" style="left:602px;top:198px">Social</h4>
  <ul class="social-list">
    <li><span class="dot"></span>Like us on Friendspace</li>
    <li><span class="dot"></span>Follow us on Chirper</li>
    <li><span class="dot"></span>Add us in WorkLink</li>
  </ul>
</footer>

<div class="legal-bar">
  <span class="copyright">Copyright 2013 © KLV Home Loans - All Rights Reserved</span>
  <div class="legal-links">
    <a href="#">Site Map</a><span class="sep">•</span>
    <a href="#">Privacy Policy</a><span class="sep">•</span>
    <a href="#">Disclaimer</a>
  </div>
</div>

</body>
</html>
```